Business Card

We need a business card designed using one of the attached logo designs (our preference is for the boxes version, but if you think it looks better with the horizontal version we will consider those too). Standard business card dimensions.

Details that need to be included:

Lewis Marsh
Quorvane S.L.U
lewis@quorvane.com

Phone numbers:
(UK) +44 731 4602 385
(Spain) +34 615 480 327

Twitter: @Quorvane
Web: http://www.quorvane.com

Tagline (optional, if it doesnt make it look too cluttered):
Automation and configuration management specialists
or
Configuration management specialists

```html
<!DOCTYPE html>
<html lang="en">
<head>
<meta charset="utf-8">
<title>Quorvane Business Card</title>
<link rel="stylesheet" href="https://fonts.googleapis.com/css2?family=Roboto:wght@300;400;700&display=swap">
<style>
  :root {
    --page-bg: #e6e6ea;
    --card-white: #fbfbfb;
    --blue-light: #1fc0f1;
    --blue-deep: #2f84c8;
    --mark-blue: #2a92d6;
    --wordmark: #1c1c1e;
    --text-on-blue: #ffffff;
  }
  * { margin: 0; padding: 0; box-sizing: border-box; }
  html, body {
    width: 1200px;
    height: 900px;
    overflow: hidden;
    background: var(--page-bg);
    font-family: "Roboto", Arial, sans-serif;
  }
  .business-card {
    position: absolute;
    left: 160px;
    top: 200px;
    width: 880px;
    height: 500px;
    display: flex;
    box-shadow: 0 10px 30px rgba(0, 0, 0, 0.18);
  }
  .brand-panel {
    width: 450px;
    height: 100%;
    background: var(--card-white);
    display: flex;
    flex-direction: column;
    align-items: center;
    padding-top: 104px;
  }
  .brand-square {
    width: 210px;
    height: 210px;
    border-radius: 22px;
    background: var(--mark-blue);
  }
  .brand-name {
    margin-top: 26px;
    font-size: 38px;
    font-weight: 700;
    letter-spacing: 2px;
    color: var(--wordmark);
  }
  .contact-panel {
    position: relative;
    flex: 1;
    height: 100%;
    background: linear-gradient(90deg, var(--blue-light) 0%, var(--blue-deep) 100%);
    color: var(--text-on-blue);
  }
  .person-name {
    position: absolute;
    top: 168px;
    left: 0;
    width: 100%;
    text-align: center;
    font-size: 66px;
    font-weight: 300;
    line-height: 1;
  }
  .company-name {
    position: absolute;
    top: 252px;
    left: 0;
    width: 100%;
    text-align: center;
    font-size: 31px;
    font-weight: 300;
    line-height: 1;
  }
  .contact-details {
    position: absolute;
    left: 56px;
    top: 410px;
    display: grid;
    grid-template-columns: auto auto;
    grid-auto-rows: 24px;
    column-gap: 18px;
    font-size: 14px;
    font-weight: 400;
    line-height: 1;
    white-space: nowrap;
  }
  .contact-item {
    display: flex;
    align-items: center;
    gap: 6px;
  }
  .icon { width: 14px; height: 14px; flex: none; }
  .label { font-size: 12px; margin-right: 4px; }
</style>
</head>
<body>
  <div class="business-card">
    <div class="brand-panel">
      <div class="brand-square"></div>
      <div class="brand-name">QUORVANE</div>
    </div>
    <div class="contact-panel">
      <div class="person-name">Lewis Marsh</div>
      <div class="company-name">Quorvane S.L.U</div>
      <div class="contact-details">
        <div class="contact-item">
          <svg class="icon" viewBox="0 0 14 14"><rect x="1" y="3" width="12" height="8" fill="none" stroke="#fff" stroke-width="1.3"/><path d="M1 3 L7 8 L13 3" fill="none" stroke="#fff" stroke-width="1.3"/></svg>
          <span>lewis@quorvane.com</span>
        </div>
        <div class="contact-item">
          <svg class="icon" viewBox="0 0 14 14"><circle cx="7" cy="7" r="5.6" fill="none" stroke="#fff" stroke-width="1.3"/><ellipse cx="7" cy="7" rx="2.4" ry="5.6" fill="none" stroke="#fff" stroke-width="1"/><line x1="1.4" y1="7" x2="12.6" y2="7" stroke="#fff" stroke-width="1"/></svg>
          <span>www.quorvane.com</span>
        </div>
        <div class="contact-item">
          <svg class="icon" viewBox="0 0 14 14"><rect x="3.5" y="0.8" width="7" height="12.4" rx="1.4" fill="none" stroke="#fff" stroke-width="1.3"/><circle cx="7" cy="11" r="0.8" fill="#fff"/></svg>
          <span><span class="label">(UK)</span>+44 731 4602 385</span>
        </div>
        <div class="contact-item">
          <span><span class="label">(Spain)</span>+34 615 480 327</span>
        </div>
        <div class="contact-item">
          <svg class="icon" viewBox="0 0 14 14"><circle cx="7" cy="7" r="4.5" fill="#fff"/></svg>
          <span>@Quorvane</span>
        </div>
      </div>
    </div>
  </div>
</body>
</html>
```